Postcard Design

KVO Ltd are a screen and large format digital company that specialise is direct to substrate marketing. I would like a postcard design to send to clients with every job we send out, informing them of other items we can do.
From conventional screen printing to digital printing from vehicle graphics to glass printing, from exhibition panels to window graphics, banners etc.
You can read more on our web site www.kvo-ltd.com
Emphasis on dealing directly with the printers instead of using a middle marketing company
we like the back to be a reply card , with the logo but like the idea or the paper looking scrunched up as in the brisk lantern advert.
hi re logo to be used as supplied

Target Market(s)

Other printers who we trade print for and Marketing agencies

Industry/Entity Type

Screen Printing

Requirements
Must have
• Company logo
Nice to have
• Something different.......BE BOLD, almost quirky
Should not have
• the usual Printers CMYK cack

```html
<!DOCTYPE html>
<html lang="en">
<head>
<meta charset="utf-8">
<title>KVO Ltd Postcard</title>
<link rel="stylesheet" href="https://fonts.googleapis.com/css2?family=Anton&family=Jost:wght@400;500&display=swap">
<style>
  :root {
    --page: #ffffff;
    --label: #8a8a8a;
    --ink: #3a1f0c;
    --toast-light: #f6dfa8;
    --toast-mid: #e7b465;
    --toast-dark: #c9842f;
    --frame: #7c7c7c;
    --cream: #fff2d9;
    --logo-disc: #3cb3e3;
    --logo-text: #3b3b3b;
    --stamp-text: #222222;
  }
  * { margin: 0; padding: 0; box-sizing: border-box; }
  html, body {
    width: 868px;
    height: 1200px;
    overflow: hidden;
    background: var(--page);
    font-family: "Jost", sans-serif;
  }
  .canvas {
    position: relative;
    width: 868px;
    height: 1200px;
  }
  .side-label {
    position: absolute;
    left: 100px;
    font-size: 19px;
    font-weight: 400;
    color: var(--label);
    letter-spacing: 0.2px;
  }
  .side-label--face { top: 20px; }
  .side-label--back { top: 602px; }

  /* Front of the card */
  .face {
    position: absolute;
    left: 96px;
    top: 49px;
    width: 674px;
    height: 521px;
    overflow: hidden;
  }
  .face__photo {
    position: absolute;
    inset: 0;
    background:
      radial-gradient(ellipse at 30% 35%, var(--toast-light) 0%, transparent 45%),
      radial-gradient(ellipse at 70% 60%, var(--toast-light) 0%, transparent 40%),
      radial-gradient(ellipse at 50% 50%, var(--toast-mid) 30%, var(--toast-dark) 100%);
  }
  .face__headline {
    position: absolute;
    inset: 0;
  }
  .face__headline text {
    font-family: "Anton", sans-serif;
    font-size: 82px;
    fill: var(--ink);
  }

  /* Reply side */
  .back {
    position: absolute;
    left: 96px;
    top: 629px;
    width: 674px;
    height: 524px;
    border: 1px solid var(--frame);
    background: var(--page);
  }
  .brand {
    position: absolute;
    left: 45px;
    top: 25px;
    display: flex;
    align-items: center;
    gap: 14px;
  }
  .brand__disc {
    width: 124px;
    height: 124px;
    border-radius: 50%;
    background: var(--logo-disc);
  }
  .brand__name {
    font-family: "Jost", sans-serif;
    font-size: 30px;
    font-weight: 500;
    color: var(--logo-text);
  }
  .stamp {
    position: absolute;
    left: 516px;
    top: 18px;
    width: 131px;
    height: 156px;
  }
  .stamp text {
    font-family: "Jost", sans-serif;
    font-size: 9px;
    fill: var(--stamp-text);
    letter-spacing: 0.2px;
  }
  .message-box {
    position: absolute;
    left: 17px;
    top: 180px;
    width: 310px;
    height: 252px;
    border-radius: 15px;
    background: var(--cream);
  }
  .address-line {
    position: absolute;
    height: 27px;
    border-radius: 11px;
    background: var(--cream);
  }
  .address-line--1 { left: 472px; top: 322px; width: 184px; }
  .address-line--2 { left: 360px; top: 363px; width: 296px; }
  .address-line--3 { left: 360px; top: 404px; width: 296px; }
</style>
</head>
<body>
<main class="canvas">
  <p class="side-label side-label--face">face</p>

  <section class="face">
    <div class="face__photo" role="img" aria-label="Close-up photograph of a slice of golden toasted bread filling the card"></div>
    <svg class="face__headline" width="674" height="521" viewBox="0 0 674 521">
      <g transform="rotate(-2.7 337 460)">
        <text x="-4" y="420" textLength="684" lengthAdjust="spacingAndGlyphs">DON’T LET YOUR</text>
        <text x="-4" y="506" textLength="684" lengthAdjust="spacingAndGlyphs">PRINTS BE DREAMS</text>
      </g>
    </svg>
  </section>

  <p class="side-label side-label--back">back</p>

  <section class="back">
    <div class="brand">
      <div class="brand__disc"></div>
      <span class="brand__name">KVO Ltd</span>
    </div>

    <svg class="stamp" width="131" height="156" viewBox="0 0 131 156">
      <text x="118" y="9" text-anchor="end">★THE LATEST IN</text>
      <text transform="translate(121 14) rotate(90)">DIGITAL PRINT TECHNOLOGY</text>
      <text transform="translate(13 147) rotate(180)" text-anchor="end">★THE LATEST IN</text>
      <text transform="translate(10 142) rotate(-90)">DIGITAL PRINT TECHNOLOGY</text>
    </svg>

    <div class="message-box"></div>
    <div class="address-line address-line--1"></div>
    <div class="address-line address-line--2"></div>
    <div class="address-line address-line--3"></div>
  </section>
</main>
</body>
</html>
```